GIF Dynamic for Marketing Agency

Need a Dynamic GIF Created for Web Banner Placement. This is to Promote the Company, It's Products and Services on a Web Directory. Needs to contain a Creative Button/Call to Action such as 'Get Leads'

About the Company: Company is a Lead Generation Company Servicing Business Finance Professionals. Company Provides the Following Primary Products and Services:

-Lead Generation
-Live Calls
-Appointments
-Ads Management
-Aged Leads
-B2B Data
(2) Sizes: 250x250(Desktop) & 728 x 90 (Mobile)

*RECOMMENDED. Visit Company Website (See Logo) to Understand its Products & Services to develop insights as to what the company is looking for.

Target Market(s)

Business Loan Brokers

Industry/Entity Type

Marketing

Colors
0054AA
0677BA
7BADD7
CADEEF
E8F1F8
0094D4
00A9DD
6FCCEA
C7EBF8
E9F6FB
FFF300
FFF600
FEFA6F
FFFEC7
FFFEE8
EE7325
F08F49
F5BC92
FAE3D3
FDF4ED

Requirements
Must have
• Dynamic GIF. 2 Sizes. 250x250 & 728x90. CREATIVITY. Call to Action. Unique, Professional & Modern.
Nice to have
• Colorful
Should not have
• No Clipart Whatsoever.

```html
<!DOCTYPE html>
<html lang="en">
<head>
<meta charset="utf-8">
<title>Northline Leads – Banner</title>
<link rel="stylesheet" href="https://fonts.googleapis.com/css2?family=Nunito:wght@800;900&display=swap">
<style>
  :root {
    --orange: #ee7325;
    --orange-mid: #f08f49;
    --orange-soft: #fae3d3;
    --orange-deep: #d9621a;
    --sky: #00a9dd;
    --sky-light: #c7ebf8;
    --sky-pale: #e9f6fb;
    --blue-soft: #7badd7;
    --blue: #0054aa;
    --yellow: #fff300;
    --navy: #1d2733;
    --white: #ffffff;
  }
  * { margin: 0; padding: 0; box-sizing: border-box; }
  html, body { width: 1200px; height: 148px; overflow: hidden; background: var(--white); }
  .banner {
    position: relative;
    width: 1200px;
    height: 148px;
    overflow: hidden;
    font-family: "Nunito", "Arial Rounded MT Bold", sans-serif;
    background: var(--white);
  }
  .banner__glow-left {
    position: absolute; left: 0; top: 0; width: 330px; height: 148px;
    background: linear-gradient(90deg, var(--orange) 0%, var(--orange-mid) 30%, var(--orange-soft) 62%, rgba(255,255,255,0) 100%);
  }
  .banner__sky-right { position: absolute; right: 0; top: 0; width: 300px; height: 148px; }

  .brand {
    position: absolute; left: 14px; top: 9px; width: 100px; height: 130px;
    background: var(--navy);
    display: flex; align-items: center; justify-content: center; text-align: center;
    padding: 8px;
  }
  .brand__name {
    color: var(--white); font-weight: 900; font-size: 15px; line-height: 1.2;
    text-transform: uppercase; letter-spacing: 0.3px;
  }

  .services {
    position: absolute; left: 208px; top: 18px;
    display: grid; grid-template-columns: 336px 336px; grid-auto-rows: 37px;
    list-style: none;
  }
  .service {
    display: flex; align-items: center; gap: 14px;
    color: var(--sky); font-weight: 800; font-size: 34px; line-height: 1; white-space: nowrap;
  }
  .service__tick { width: 25px; height: 25px; flex: none; }

  .cta {
    position: absolute; left: 968px; top: 44px; width: 200px; height: 60px;
    display: flex; align-items: center; justify-content: center; gap: 10px;
    border-radius: 30px;
    background: linear-gradient(180deg, var(--orange-mid) 0%, var(--orange) 55%, var(--orange-deep) 100%);
    box-shadow: 0 4px 10px rgba(0, 84, 170, 0.3);
    color: var(--white); font-weight: 900; font-size: 26px; line-height: 1;
    text-decoration: none; white-space: nowrap;
    animation: cta-pulse 1.6s ease-in-out infinite;
  }
  .cta__arrow { width: 24px; height: 24px; flex: none; animation: cta-nudge 1.6s ease-in-out infinite; }
  @keyframes cta-pulse {
    0%, 100% { transform: scale(1); box-shadow: 0 4px 10px rgba(0, 84, 170, 0.3); }
    50% { transform: scale(1.05); box-shadow: 0 6px 16px rgba(0, 84, 170, 0.4); }
  }
  @keyframes cta-nudge {
    0%, 100% { transform: translateX(0); }
    50% { transform: translateX(4px); }
  }
</style>
</head>
<body>
<div class="banner">
  <div class="banner__glow-left"></div>

  <svg class="banner__sky-right" viewBox="0 0 300 148" aria-hidden="true">
    <defs>
      <linearGradient id="skyFade" x1="0" x2="1" y1="0" y2="0">
        <stop offset="0" stop-color="#e9f6fb" stop-opacity="0"/>
        <stop offset="0.4" stop-color="#c7ebf8"/>
        <stop offset="1" stop-color="#7badd7"/>
      </linearGradient>
      <linearGradient id="skyBand" x1="0" x2="1" y1="0" y2="1">
        <stop offset="0" stop-color="#ffffff" stop-opacity="0.9"/>
        <stop offset="1" stop-color="#e9f6fb" stop-opacity="0.2"/>
      </linearGradient>
    </defs>
    <rect width="300" height="148" fill="url(#skyFade)"/>
    <polygon points="120,0 190,0 110,148 40,148" fill="url(#skyBand)"/>
    <polygon points="230,0 260,0 200,148 170,148" fill="#ffffff" opacity="0.35"/>
  </svg>

  <div class="brand">
    <span class="brand__name">Northline Leads</span>
  </div>

  <ul class="services">
    <li class="service"><svg class="service__tick" viewBox="0 0 28 28" aria-hidden="true"><circle cx="14" cy="14" r="13" fill="var(--orange)"/><path d="M7.5 14.5l4.5 4.5 8.5-9.5" fill="none" stroke="#fff" stroke-width="3.4" stroke-linecap="round" stroke-linejoin="round"/></svg>Lead Generation</li>
    <li class="service"><svg class="service__tick" viewBox="0 0 28 28" aria-hidden="true"><circle cx="14" cy="14" r="13" fill="var(--orange)"/><path d="M7.5 14.5l4.5 4.5 8.5-9.5" fill="none" stroke="#fff" stroke-width="3.4" stroke-linecap="round" stroke-linejoin="round"/></svg>Ads Management</li>
    <li class="service"><svg class="service__tick" viewBox="0 0 28 28" aria-hidden="true"><circle cx="14" cy="14" r="13" fill="var(--orange)"/><path d="M7.5 14.5l4.5 4.5 8.5-9.5" fill="none" stroke="#fff" stroke-width="3.4" stroke-linecap="round" stroke-linejoin="round"/></svg>Live Calls</li>
    <li class="service"><svg class="service__tick" viewBox="0 0 28 28" aria-hidden="true"><circle cx="14" cy="14" r="13" fill="var(--orange)"/><path d="M7.5 14.5l4.5 4.5 8.5-9.5" fill="none" stroke="#fff" stroke-width="3.4" stroke-linecap="round" stroke-linejoin="round"/></svg>Aged Leads</li>
    <li class="service"><svg class="service__tick" viewBox="0 0 28 28" aria-hidden="true"><circle cx="14" cy="14" r="13" fill="var(--orange)"/><path d="M7.5 14.5l4.5 4.5 8.5-9.5" fill="none" stroke="#fff" stroke-width="3.4" stroke-linecap="round" stroke-linejoin="round"/></svg>Appointments</li>
    <li class="service"><svg class="service__tick" viewBox="0 0 28 28" aria-hidden="true"><circle cx="14" cy="14" r="13" fill="var(--orange)"/><path d="M7.5 14.5l4.5 4.5 8.5-9.5" fill="none" stroke="#fff" stroke-width="3.4" stroke-linecap="round" stroke-linejoin="round"/></svg>B2B Data</li>
  </ul>

  <a class="cta" href="#get-leads">Get Leads<svg class="cta__arrow" viewBox="0 0 24 24" aria-hidden="true"><circle cx="12" cy="12" r="11" fill="var(--white)"/><path d="M9.5 7l5 5-5 5" fill="none" stroke="var(--orange)" stroke-width="3" stroke-linecap="round" stroke-linejoin="round"/></svg></a>
</div>
</body>
</html>
```